Business Card Design

We need a business card designed for our new company. Prefer a black card with white logo & writing.

Contact Information for Business Card

Dale Pickett, address: 7-4417 Larchmere Avenue, Abbotsford, BC, V3K 2R9, Office Phone: 604-555-0172, Cell: 604-555-0138, Email: dale@kelsoncoatworks.ca

Colors

Designer to choose only greyscale colors for use in the design.

```html
<!DOCTYPE html>
<html lang="en">
<head>
<meta charset="utf-8">
<title>Kelson Coatworks – Business Card</title>
<link href="https://fonts.googleapis.com/css2?family=Fira+Sans:wght@400;600&display=swap" rel="stylesheet">
<style>
  :root {
    --page-bg: #e6e7e8;
    --card-bg: #353335;
    --band: #808080;
    --ink: #ffffff;
  }
  * { margin: 0; padding: 0; box-sizing: border-box; }
  html, body {
    width: 1200px; height: 1200px; overflow: hidden;
    background: var(--page-bg);
    font-family: "Fira Sans", sans-serif;
    color: var(--ink);
  }
  .card {
    position: absolute; left: 220px;
    width: 760px; height: 421px;
    background: var(--card-bg);
  }
  .card--front { top: 150px; }
  .card--back { top: 628px; }
  .card__band {
    position: absolute; left: 0; width: 100%; height: 20px;
    background: var(--band);
  }
  .card__band--top { top: 0; }
  .card__band--bottom { bottom: 0; }
  .card__rule {
    position: absolute; left: 0; width: 100%; height: 3px;
    background: var(--ink);
  }
  .card__rule--top { top: 23px; }
  .card__rule--bottom { bottom: 23px; }

  .brand {
    position: absolute;
    display: flex; flex-direction: column; align-items: center;
    text-align: center; font-weight: 600; line-height: 1;
    transform: translate(-50%, -50%);
  }
  .brand__mark {
    width: 14px; height: 14px; background: var(--ink); margin-bottom: 12px;
  }
  .brand__name { letter-spacing: 0.06em; }
  .brand--small { left: 180px; top: 214px; font-size: 32px; }
  .brand--large { left: 380px; top: 212px; font-size: 46px; }
  .brand--large .brand__mark { width: 18px; height: 18px; margin-bottom: 16px; }

  .holder {
    position: absolute; left: 358px; top: 88px; width: 348px;
  }
  .holder__name {
    font-size: 56px; font-weight: 600; line-height: 1;
    padding-left: 4px;
  }
  .holder__rule {
    height: 3px; background: var(--ink); margin-top: 14px; margin-left: -4px;
  }
  .contact {
    margin-top: 22px;
    display: grid; grid-template-columns: 116px 1fr;
    row-gap: 10px; font-size: 17.5px; line-height: 21px; font-weight: 400;
  }
  .contact__value::before { content: ": "; }
  .contact__value--cont { padding-left: 10px; }
</style>
</head>
<body>
  <section class="card card--front">
    <div class="card__band card__band--top"></div>
    <div class="card__rule card__rule--top"></div>

    <div class="brand brand--small">
      <span class="brand__mark"></span>
      <span class="brand__name">KELSON</span>
      <span class="brand__name">COATWORKS</span>
    </div>

    <div class="holder">
      <h1 class="holder__name">Dale Pickett</h1>
      <div class="holder__rule"></div>
      <div class="contact">
        <span class="contact__label">Office Phone</span>
        <span class="contact__value">604-555-0172</span>
        <span class="contact__label">Cell</span>
        <span class="contact__value">604-555-0138</span>
        <span class="contact__label">Email</span>
        <span class="contact__value">dale@kelsoncoatworks.ca</span>
        <span class="contact__label">address</span>
        <span class="contact__value">7-4417 Larchmere Avenue,</span>
        <span></span>
        <span class="contact__value--cont">Abbotsford, BC, V3K 2R9</span>
      </div>
    </div>

    <div class="card__rule card__rule--bottom"></div>
    <div class="card__band card__band--bottom"></div>
  </section>

  <section class="card card--back">
    <div class="card__band card__band--top"></div>
    <div class="card__rule card__rule--top"></div>

    <div class="brand brand--large">
      <span class="brand__mark"></span>
      <span class="brand__name">KELSON</span>
      <span class="brand__name">COATWORKS</span>
    </div>

    <div class="card__rule card__rule--bottom"></div>
    <div class="card__band card__band--bottom"></div>
  </section>
</body>
</html>
```